Re-drawing and gpahically, according to coorporate design

Three flowcharts need to be re-drawn and graphically improved according to coorporate design

```html
<!DOCTYPE html>
<html lang="en">
<head>
<meta charset="utf-8">
<title>Flowchart redesign – three slides</title>
<link href="https://fonts.googleapis.com/css2?family=Open+Sans:wght@300;400;600;700&family=Arimo:wght@400;700&family=Roboto+Mono:wght@700&display=swap" rel="stylesheet">
<style>
  :root{
    --olive:#b5b03a;
    --olive-text:#a3ab25;
    --brand:#8c9a2e;
    --grey:#7b7b7b;
    --grey-dark:#5f6468;
    --green:#76b043;
    --green-dark:#4f7a32;
    --agri:#5b8a3a;
    --brown:#6b4226;
    --blue:#5b8fd0;
    --blue-line:#2f4fa8;
    --navy:#24308a;
    --h2:#8fa8d8;
    --orange:#e8a21a;
    --orange-line:#f4b41e;
    --module-blue:#3b7bbf;
    --module-green:#5f9a35;
    --module-red:#e0702a;
    --text:#444;
  }
  *{box-sizing:border-box;margin:0;padding:0}
  html,body{width:864px;height:1200px;overflow:hidden;background:#fff}
  body{position:relative;font-family:"Open Sans",sans-serif;color:var(--text)}

  .slide{position:absolute;left:195px;width:452px;height:339px;border:1px solid #111;overflow:hidden;background:#fff}
  .slide--diagram{top:35px}
  .slide--ideas{top:415px}
  .slide--samba{top:798px}
  .slide__canvas{position:absolute;left:0;top:0;width:866px;height:648px;transform:scale(0.5208);transform-origin:0 0}

  .header{position:absolute;left:0;top:0;width:866px;height:78px;border-bottom:1px solid #e6e6e6}
  .brand{position:absolute;left:32px;top:22px;display:flex;align-items:flex-start;gap:8px}
  .brand__dot{width:34px;height:34px;border-radius:50%;background:var(--grey);margin-top:6px}
  .brand__name{font-weight:700;font-size:29px;line-height:30px;color:var(--brand);letter-spacing:.5px}
  .brand__sub{font-size:15px;color:#555;line-height:18px;font-weight:400}
  .uni{position:absolute;right:32px;top:30px;display:flex;align-items:center;gap:6px}
  .uni__square{width:14px;height:14px;background:var(--grey-dark)}
  .uni__name{font-weight:700;font-size:15px;color:var(--grey-dark);letter-spacing:.5px}
  .footer-band{position:absolute;left:0;width:866px;height:27px;background:var(--olive)}

  .diagram{position:absolute;left:0;top:0;width:866px;height:648px}
  .diagram text{font-family:"Arimo",sans-serif;font-size:9px;fill:#fff}

  .ideas__title{position:absolute;left:39px;top:134px;font-weight:700;font-size:20px;color:var(--olive-text)}
  .ideas__list{position:absolute;left:55px;top:196px;width:300px;list-style:none}
  .ideas__list li{position:relative;padding-left:24px;font-size:10.5px;line-height:13.5px;color:#6a6a6a;text-align:justify;margin-bottom:14px}
  .ideas__list li::before{content:"";position:absolute;left:0;top:3px;width:8px;height:8px;border-radius:50%;background:#6a6a6a}
  .reference{position:absolute;left:402px;top:192px;width:416px;height:312px;background:var(--olive);padding:12px}
  .reference__inner{width:100%;height:100%;background:#fff;padding:10px 12px}
  .reference__title{font-family:"Roboto Mono",monospace;font-weight:700;font-size:15.5px;color:#111;text-align:center;white-space:nowrap}
  .reference__graphic{margin-top:8px;height:238px;border-radius:4px;background:radial-gradient(ellipse at 50% 55%,#eef0ea 0%,#e3ecd9 35%,#dbe7f1 60%,#f4f4f4 100%)}

  .samba{position:absolute;inset:0;font-family:"Arimo",sans-serif}
  .box{position:absolute;text-align:center;font-size:7.5px;line-height:10px}
  .box b{display:block;font-weight:700}
  .samba__head{left:182px;top:118px;width:449px;height:54px;background:#dcdfe3;border:1px solid #c6c9cd;border-radius:3px;padding-top:9px}
  .samba__title{font-size:12px;font-weight:700;color:var(--module-blue)}
  .samba__sub{font-size:7.5px;font-style:italic;font-weight:700;color:var(--module-blue);margin-top:6px}
  .samba__sub span{color:var(--orange)}
  .frame{position:absolute;border:1.5px dashed #b9b9b9;border-radius:4px}
  .m1{left:196px;top:180px;width:449px;height:27px;background:#fdf3cf;color:var(--orange);border-radius:3px;padding-top:3px}
  .m2{left:196px;top:232px;width:449px;height:26px;background:#d6e2f3;color:var(--module-blue);border-radius:3px;padding-top:3px}
  .m3{left:196px;top:334px;width:449px;height:26px;background:#dfeccd;color:var(--module-green);border-radius:3px;padding-top:3px}
  .m4{left:183px;top:475px;width:448px;height:27px;background:#fbe3d3;color:var(--module-red);border-radius:3px;padding-top:3px}
  .sub{border:1px solid #c9c9c9;border-radius:3px;background:#fff;padding-top:6px}
  .sub--blue{color:var(--module-blue)}
  .sub--green{color:var(--module-green)}
  .sub--red{color:var(--module-red)}
  .assess{left:196px;top:409px;width:449px;height:35px;border:1px solid #c9c9c9;border-radius:3px;background:linear-gradient(90deg,#e6f0dc,#fff 40%);color:var(--module-green);text-align:left;padding:3px 0 0 60px;display:flex;gap:8px}
  .assess__label{font-weight:700;padding-top:2px}
  .assess__lines{line-height:10px}
</style>
</head>
<body>

<!-- Slide 1: carbon flow diagram -->
<section class="slide slide--diagram">
  <div class="slide__canvas">
    <header class="header">
      <div class="brand"><span class="brand__dot"></span><div><div class="brand__name">VOLTAHAUS INSTITUT</div><div class="brand__sub">at Nordtal University</div></div></div>
      <div class="uni"><span class="uni__square"></span><span class="uni__name">NORDTAL UNIVERSITY</span></div>
    </header>

    <svg class="diagram" viewBox="0 0 866 648" aria-label="Flow of biomass, CO2 and hydrogen into products">
      <defs>
        <radialGradient id="sunGrad"><stop offset="0" stop-color="#ffe14a"/><stop offset="1" stop-color="#f6a21c"/></radialGradient>
      </defs>
      <g fill="none" stroke="#6aaa3a" stroke-width="1">
        <path d="M166 142H279" stroke="#f3a63a"/>
        <path d="M136 172V203" stroke="#f3a63a"/>
        <path d="M398 142H452"/>
        <path d="M327 158V200H400M520 158V200H452"/>
        <path d="M571 142H601V117H656M601 142V168H656"/>
        <path d="M426 221V235M325 235H540M325 235V251M430 235V251M535 235V251"/>
        <path d="M288 274H250"/>
        <path d="M572 274H602M602 224V325M602 224H656M602 274H656M602 325H656"/>
        <path d="M325 303V345H405M430 303V318M528 303V345H447"/>
      </g>
      <g fill="none" stroke="var(--blue-line)" stroke-width="1">
        <path d="M405 339H290V427H280"/>
        <path d="M426 360V383M345 383H662M345 383V400M452 383V400M557 383V400M662 383V400"/>
        <path d="M157 376H240V400"/>
        <path d="M240 455V484M345 455V484M452 455V484M557 455V484M664 455V484"/>
      </g>
      <g fill="none" stroke="#5b8fd0" stroke-width="1">
        <path d="M135 247V275M135 320V354M135 398V429"/>
      </g>

      <circle cx="136" cy="142" r="30" fill="url(#sunGrad)" role="img" aria-label="Sun as energy source"/>

      <rect x="279" y="126" width="119" height="32" rx="16" fill="var(--agri)" stroke="#3d8f8f" stroke-width="2"/>
      <text x="338" y="139" text-anchor="middle" font-size="11">agriculture/</text>
      <text x="325" y="151" text-anchor="middle" font-size="11">forestry</text>
      <rect x="452" y="126" width="119" height="32" rx="16" fill="var(--grey)" stroke="#555" stroke-width="2"/>
      <text x="511" y="147" text-anchor="middle" font-size="11">industry</text>

      <circle cx="426" cy="195" r="26" fill="#6f8f4f"/>
      <text x="426" y="198" text-anchor="middle">residues</text>

      <circle cx="678" cy="117" r="22" fill="var(--green-dark)"/>
      <text x="678" y="120" text-anchor="middle" font-size="8.5">food/feed</text>
      <circle cx="678" cy="168" r="22" fill="var(--brown)"/>
      <text x="664" y="160" font-size="8.5">wood</text><text x="664" y="170" font-size="8.5">base</text><text x="664" y="180" font-size="8.5">product</text>

      <circle cx="135" cy="225" r="22" fill="var(--grey)"/>
      <text x="135" y="223" text-anchor="middle" font-size="8">renewable</text>
      <text x="135" y="232" text-anchor="middle" font-size="8">electricity</text>

      <rect x="199" y="221" width="80" height="21" fill="#fff" stroke="#999"/>
      <text x="239" y="235" text-anchor="middle" fill="#666" style="fill:#666">Cleaner Gas Grid</text>

      <circle cx="228" cy="274" r="22" fill="#6aaa3a"/>
      <text x="228" y="277" text-anchor="middle">CH4</text>

      <g fill="var(--green)">
        <path d="M288 257V303A37 6 0 0 0 362 303V257Z"/><ellipse cx="325" cy="257" rx="37" ry="6" fill="#8dc45c"/>
        <path d="M393 257V303A37 6 0 0 0 467 303V257Z"/><ellipse cx="430" cy="257" rx="37" ry="6" fill="#8dc45c"/>
        <path d="M498 257V303A37 6 0 0 0 572 303V257Z"/><ellipse cx="535" cy="257" rx="37" ry="6" fill="#8dc45c"/>
      </g>
      <text x="325" y="282" text-anchor="middle">anaerobic</text><text x="325" y="292" text-anchor="middle">digestion</text>
      <text x="430" y="282" text-anchor="middle">biomass</text><text x="430" y="292" text-anchor="middle">gasification</text>
      <text x="535" y="286" text-anchor="middle">fermentation</text>

      <path d="M97 281V320A37 6 0 0 0 172 320V281Z" fill="var(--grey)"/><ellipse cx="135" cy="281" rx="37" ry="6" fill="#999"/>
      <text x="135" y="308" text-anchor="middle">electrolysis</text>

      <circle cx="678" cy="224" r="22" fill="#6aaa3a"/><text x="678" y="227" text-anchor="middle" font-size="8.5">poly-mers</text>
      <circle cx="678" cy="274" r="22" fill="#6aaa3a"/><text x="678" y="277" text-anchor="middle" font-size="8.5">chemi-cals</text>
      <circle cx="678" cy="325" r="22" fill="#6aaa3a"/><text x="678" y="328" text-anchor="middle">fuels</text>

      <circle cx="426" cy="339" r="21" fill="var(--navy)" stroke="#3a6fb0" stroke-width="1.5"/>
      <text x="426" y="342" text-anchor="middle">CO2</text>

      <circle cx="135" cy="376" r="22" fill="var(--h2)"/>
      <text x="135" y="379" text-anchor="middle">H2</text>

      <g fill="var(--blue)">
        <path d="M203 406V455A37 6 0 0 0 278 455V406Z"/><ellipse cx="240" cy="406" rx="37" ry="6" fill="#7fa9dc"/>
        <path d="M307 406V455A37 6 0 0 0 382 455V406Z"/><ellipse cx="345" cy="406" rx="37" ry="6" fill="#7fa9dc"/>
        <path d="M414 406V455A37 6 0 0 0 489 455V406Z"/><ellipse cx="452" cy="406" rx="37" ry="6" fill="#7fa9dc"/>
        <path d="M519 406V455A37 6 0 0 0 594 455V406Z"/><ellipse cx="557" cy="406" rx="37" ry="6" fill="#7fa9dc"/>
      </g>
      <path d="M624 406V455A37 6 0 0 0 699 455V406Z" fill="var(--green)"/><ellipse cx="662" cy="406" rx="37" ry="6" fill="#8dc45c"/>
      <text x="214" y="428">catalytic/</text><text x="214" y="438">biological</text><text x="214" y="448">methanation</text>
      <text x="322" y="428">electro-</text><text x="322" y="438">chemical</text><text x="322" y="448">conversion</text>
      <text x="424" y="428" font-size="8">other</text><text x="424" y="437" font-size="8">chemical</text><text x="424" y="446" font-size="7.5">transformations</text>
      <text x="533" y="430">existing</text><text x="533" y="440">industrial</text><text x="533" y="450">applications</text>
      <text x="662" y="439" text-anchor="middle">algea</text>

      <path d="M97 435V498A37 6 0 0 0 172 498V435Z" fill="var(--grey)"/><ellipse cx="135" cy="435" rx="37" ry="6" fill="#999"/>
      <text x="106" y="460" font-size="7.5">various direct</text><text x="106" y="470" font-size="7.5">applications-</text><text x="106" y="480" font-size="7.5">mobility-</text><text x="106" y="490" font-size="7.5">industry-gas grid</text>

      <circle cx="241" cy="506" r="22" fill="var(--blue)"/><text x="241" y="509" text-anchor="middle">CH4</text>
      <circle cx="345" cy="506" r="22" fill="var(--blue)"/>
      <text x="345" y="495" font-size="7" text-anchor="middle">e.g.</text><text x="345" y="503" font-size="7" text-anchor="middle">ethylene-</text><text x="345" y="511" font-size="7" text-anchor="middle">oxide</text><text x="345" y="519" font-size="7" text-anchor="middle">C2H4O</text>
      <circle cx="452" cy="506" r="22" fill="var(--blue)"/>
      <text x="452" y="496" font-size="7" text-anchor="middle">e.g.</text><text x="452" y="504" font-size="7" text-anchor="middle">polyols,</text><text x="452" y="512" font-size="7" text-anchor="middle">polymers,</text><text x="452" y="520" font-size="7" text-anchor="middle">etc...</text>
      <circle cx="559" cy="506" r="22" fill="var(--blue)"/>
      <text x="559" y="499" font-size="7.5" text-anchor="middle">e.g.</text><text x="559" y="508" font-size="7.5" text-anchor="middle">beverage</text><text x="559" y="517" font-size="7.5" text-anchor="middle">industry</text>
      <circle cx="664" cy="506" r="22" fill="var(--green)"/>
      <text x="664" y="498" font-size="7.5" text-anchor="middle">fuel,</text><text x="664" y="507" font-size="7.5" text-anchor="middle">bio-</text><text x="664" y="516" font-size="7.5" text-anchor="middle">polymers</text>

      <g fill="#d9d9d9">
        <rect x="729" y="206" width="26" height="22"/>
        <rect x="727" y="250" width="48" height="20"/>
        <rect x="727" y="284" width="55" height="8"/>
        <rect x="727" y="312" width="48" height="14"/>
        <rect x="727" y="335" width="48" height="14"/>
        <rect x="575" y="467" width="52" height="12"/>
        <rect x="180" y="536" width="46" height="14"/>
        <rect x="242" y="538" width="45" height="12"/>
        <rect x="180" y="558" width="42" height="14"/>
        <rect x="235" y="560" width="50" height="12"/>
        <rect x="322" y="539" width="46" height="14"/>
      </g>
    </svg>

    <div class="footer-band" style="top:605px"></div>
  </div>
</section>

<!-- Slide 2: development ideas -->
<section class="slide slide--ideas">
  <div class="slide__canvas">
    <header class="header">
      <div class="brand"><span class="brand__dot"></span><div><div class="brand__name">VOLTAHAUS INSTITUT</div><div class="brand__sub">at Nordtal University</div></div></div>
      <div class="uni"><span class="uni__square"></span><span class="uni__name">NORDTAL UNIVERSITY</span></div>
    </header>

    <h2 class="ideas__title">Ideas to further develop this graph:</h2>
    <ul class="ideas__list">
      <li>New title: “Circular Bioeconomy”</li>
      <li>The step “Agriculture” and “Processing” perhaps should share a step called “Residues” and this step should be connected with “Bioenergy &amp; Biofuels” in order to indicate that energy an biofuel production should be at the end of a biomass using cascade.</li>
      <li>Introduce CO2-flow from processing (e.g from biogas purification, fermentation processes, etc....)</li>
      <li>Introduce new step: “Power-to-Gas” and connect with the CO2-flow</li>
      <li>Introduce new step: “chemical production” and connect with CO2-flow</li>
      <li>Keep different colours for Bioeconomy and Circular Economy, use a third colour for the CO2-flows and the uptaking steps – call it “Carbon Cycle Economy” in the legend illustration?</li>
    </ul>

    <figure class="reference">
      <div class="reference__inner">
        <div class="reference__title">Bioeconomy: More than Circular Economy</div>
        <div class="reference__graphic" role="img" aria-label="Reference diagram of bioeconomy and circular economy flows between agriculture, biomass, processing, chemicals, bio-based products, food and bioenergy"></div>
      </div>
    </figure>

    <div class="footer-band" style="top:605px"></div>
  </div>
</section>

<!-- Slide 3: analysis model -->
<section class="slide slide--samba">
  <div class="slide__canvas">
    <header class="header">
      <div class="brand"><span class="brand__dot"></span><div><div class="brand__name">VOLTAHAUS INSTITUT</div><div class="brand__sub">at Nordtal University</div></div></div>
      <div class="uni"><span class="uni__square"></span><span class="uni__name">NORDTAL UNIVERSITY</span></div>
    </header>

    <div class="samba">
      <svg style="position:absolute;left:0;top:0" width="866" height="648" viewBox="0 0 866 648" aria-hidden="true">
        <g fill="none" stroke-width="1.6">
          <path d="M645 194H717V487H640M717 244H664M717 347H664" stroke="var(--orange-line)"/>
          <path d="M183 247H134V487H181M134 340H183" stroke="#5b9bd5"/>
          <path d="M196 349H146V480H181" stroke="#6aaa3a"/>
        </g>
        <g fill="var(--orange-line)"><path d="M658 241l6 3-6 3z"/><path d="M658 344l6 3-6 3z"/><path d="M640 484l-6 3 6 3z"/></g>
        <g fill="#5b9bd5"><path d="M177 244l6 3-6 3z"/><path d="M177 337l6 3-6 3z"/><path d="M175 484l6 3-6 3z"/></g>
        <path d="M175 477l6 3-6 3z" fill="#6aaa3a"/>
      </svg>

      <div class="box samba__head">
        <div class="samba__title">SCALA analysis</div>
        <div class="samba__sub"><span>S</span>ocial <span>C</span>riteria <span>A</span>nd <span>L</span>imits <span>A</span>ssessment for reducing project barriers</div>
      </div>

      <div class="box m1"><b>MODULE1</b>Starting point: product / technology / process / &nbsp;&nbsp;&nbsp;&nbsp; business model / service / vision / project</div>

      <div class="frame" style="left:183px;top:222px;width:475px;height:85px"></div>
      <div class="box m2"><b>MODULE2</b>stakeholder analysis</div>
      <div class="box sub sub--blue" style="left:184px;top:264px;width:147px;height:34px"><b>module 2a</b>identification of stakeholders</div>
      <div class="box sub sub--blue" style="left:346px;top:264px;width:161px;height:34px;padding-top:2px"><b>module 2b</b>categorizing key, primary &amp; secondary stakeholder</div>
      <div class="box sub sub--blue" style="left:508px;top:264px;width:137px;height:34px"><b>module 2c</b>identification of interests &amp; expectations</div>

      <div class="frame" style="left:183px;top:327px;width:475px;height:125px"></div>
      <div class="box m3"><b>MODULE3</b>STEEP analysis</div>
      <div class="box sub sub--green" style="left:183px;top:368px;width:88px;height:33px"><b>module 3a</b>sociological Indicators</div>
      <div class="box sub sub--green" style="left:273px;top:368px;width:88px;height:33px"><b>module 3b</b>technological Indicators</div>
      <div class="box sub sub--green" style="left:363px;top:368px;width:88px;height:33px"><b>module 3c</b>environmental Indicators</div>
      <div class="box sub sub--green" style="left:466px;top:368px;width:89px;height:33px"><b>module 3d</b>economical Indicators</div>
      <div class="box sub sub--green" style="left:556px;top:368px;width:89px;height:33px"><b>module 3e</b>political Indicators</div>
      <div class="box assess">
        <span class="assess__label">assessment:</span>
        <span class="assess__lines">+ impact of indicators on product / technology / process<br>+ impact of product / technology / process on indicators<br>+ identification of chances and risk</span>
      </div>

      <div class="frame" style="left:170px;top:470px;width:474px;height:85px"></div>
      <div class="box m4"><b>MODULE4</b>comprehensive analysis</div>
      <div class="box sub sub--red" style="left:183px;top:508px;width:148px;height:32px"><b>module 4a</b>merging of Modul 2 &amp; 3</div>
      <div class="box sub sub--red" style="left:333px;top:508px;width:160px;height:32px"><b>module 4b</b>interactions, trade-offs &amp; assessments</div>
      <div class="box sub sub--red" style="left:495px;top:508px;width:136px;height:32px"><b>module 4c</b>recommendations</div>
    </div>

    <div class="footer-band" style="top:602px"></div>
  </div>
</section>

</body>
</html>
```